Dr Peter Vandell
Urologist
Professional
Dr Peter Vandell MB,ChB(WCU), FCS Urol.(CSU)
Ridgeway Medicentre and Lanford Private Hospital PO Box 58147 Brookvale 4105
povandell@medinet-mail.co.za
Pr No 7315824
Please email me for scanned copies of the existing stationery and cards to see current format

```html
<!DOCTYPE html>
<html lang="en">
<head>
<meta charset="utf-8">
<title>Dr Peter Vandell – Stationery</title>
<link href="https://fonts.googleapis.com/css2?family=Libre+Baskerville:wght@400;700&family=Lato:wght@400;700&display=swap" rel="stylesheet">
<style>
  :root{
    --wine:#8a1c22;
    --wine-dark:#5e0f14;
    --paper:#fbf8f0;
    --ink:#3a3a3a;
    --muted:#7a7370;
    --backdrop:#ebe5da;
    --fold:#d8d2c6;
  }
  *{box-sizing:border-box;margin:0;padding:0}
  html,body{width:1200px;height:578px;overflow:hidden;background:var(--backdrop)}
  body{position:relative;font-family:"Lato",Arial,sans-serif;color:var(--ink)}
  .piece{position:absolute;background:var(--paper);box-shadow:0 2px 6px rgba(0,0,0,.25);overflow:hidden}
  .label{position:absolute;font-size:9px;color:#6d6358;font-family:"Lato",Arial,sans-serif}
  .wave{position:absolute;left:0;bottom:0;width:100%}
  .brand{position:absolute;display:flex;align-items:center;gap:6px;white-space:nowrap}
  .mark{border-radius:50%;background:var(--wine);flex:none}
  .name{font-family:"Libre Baskerville",Georgia,serif;font-weight:700;color:var(--wine);line-height:1.1}
  .quals{font-family:"Libre Baskerville",Georgia,serif;color:var(--wine);line-height:1.3}
  .role{font-family:"Libre Baskerville",Georgia,serif;font-weight:700;color:var(--wine-dark);line-height:1.2}
  .contact{position:absolute;font-size:5px;line-height:1.55;color:var(--muted);white-space:nowrap}

  /* cover sheet */
  .cover{left:34px;top:0;width:153px;height:325px;background:linear-gradient(#fff 0%,#fff 55%,rgba(255,255,255,0) 100%);box-shadow:none}
  .cover .brand{left:6px;top:24px;gap:5px}
  .cover .mark{width:28px;height:28px}
  .cover .name{font-size:12px}
  .cover .quals{font-size:5px}
  .cover .role{font-size:8.5px;margin-top:1px}

  /* business card */
  .card{left:125px;top:173px;width:156px;height:91px}
  .card .brand{left:8px;top:10px}
  .card .mark{width:18px;height:18px}
  .card .name{font-size:8px}
  .card .quals{font-size:3.5px}
  .card .role{font-size:4.5px}

  /* compliments slip */
  .slip{left:38px;top:360px;width:245px;height:173px}
  .slip .brand{left:14px;top:14px}
  .slip .mark{width:22px;height:22px}
  .slip .name{font-size:9.5px}
  .slip .quals{font-size:4px}
  .slip .role{font-size:5px}

  /* letterhead */
  .letter{left:403px;top:48px;width:317px;height:492px}
  .letter .brand{left:24px;top:22px}
  .letter .mark{width:24px;height:24px}
  .letter .name{font-size:10px}
  .letter .quals{font-size:4.2px}
  .letter .role{font-size:5.5px}
  .footer-note{position:absolute;left:20px;bottom:6px;font-size:5px;color:#fff}

  /* envelope front */
  .env-front{left:754px;top:48px;width:410px;height:211px}
  .env-front .brand{left:18px;top:14px}
  .env-front .mark{width:24px;height:24px}
  .env-front .name{font-size:10px}
  .env-front .quals{font-size:4.2px}
  .env-front .role{font-size:5.5px}

  /* envelope back */
  .env-back{left:758px;top:336px;width:399px;height:211px;background:transparent;box-shadow:0 2px 6px rgba(0,0,0,.25)}
  .env-back svg{width:100%;height:100%;display:block}
  .flap-name{font-family:"Libre Baskerville",Georgia,serif;font-weight:700;fill:var(--paper)}
</style>
</head>
<body>

<section class="piece cover">
  <div class="brand">
    <span class="mark"></span>
    <div>
      <div class="name">Dr Peter Vandell</div>
      <div class="quals">MB,ChB(WCU), FCS Urol.(CSU)</div>
      <div class="role">Urologist</div>
    </div>
  </div>
</section>

<span class="label" style="left:188px;top:162px">Card</span>
<section class="piece card">
  <div class="brand">
    <span class="mark"></span>
    <div>
      <div class="name">Dr Peter Vandell</div>
      <div class="quals">MB,ChB(WCU), FCS Urol.(CSU)</div>
      <div class="role">Urologist</div>
    </div>
  </div>
  <div class="contact" style="left:10px;top:44px">Ridgeway Medicentre<br>Lanford Private Hospital<br>Tel 033 418 6502<br>Fax 033 418 6503</div>
  <div class="contact" style="left:80px;top:44px">Pr No 7315824<br>povandell@medinet-mail.co.za<br>PO Box 58147<br>Brookvale 4105</div>
  <svg class="wave" viewBox="0 0 100 20" preserveAspectRatio="none" height="18"><path d="M0 20V13C30 3 62 19 100 5V20Z" fill="var(--wine)"/><path d="M0 11C30 1 62 17 100 3" stroke="var(--wine-dark)" stroke-width=".6" fill="none"/></svg>
</section>

<span class="label" style="left:40px;top:350px">Compliments slip</span>
<section class="piece slip">
  <div class="brand">
    <span class="mark"></span>
    <div>
      <div class="name">Dr Peter Vandell</div>
      <div class="quals">MB,ChB(WCU), FCS Urol.(CSU)</div>
      <div class="role">Urologist</div>
    </div>
  </div>
  <div class="contact" style="left:16px;top:50px">Ridgeway Medicentre<br>Lanford Private Hospital<br>PO Box 58147 Brookvale 4105<br>Tel 033 418 6502<br>povandell@medinet-mail.co.za</div>
  <svg class="wave" viewBox="0 0 100 20" preserveAspectRatio="none" height="40"><path d="M0 20V10C30 0 62 18 100 4V20Z" fill="var(--wine)"/><path d="M0 8C30-2 62 16 100 2" stroke="var(--wine-dark)" stroke-width=".5" fill="none"/></svg>
</section>

<span class="label" style="left:405px;top:38px">Letterhead</span>
<section class="piece letter">
  <div class="brand">
    <span class="mark"></span>
    <div>
      <div class="name">Dr Peter Vandell</div>
      <div class="quals">MB,ChB(WCU), FCS Urol.(CSU)</div>
      <div class="role">Urologist</div>
    </div>
  </div>
  <div class="contact" style="left:26px;top:62px">Ridgeway Medicentre<br>Lanford Private Hospital<br>PO Box 58147<br>Brookvale 4105<br>Tel 033 418 6502<br>Fax 033 418 6503<br>povandell@medinet-mail.co.za</div>
  <svg class="wave" viewBox="0 0 100 20" preserveAspectRatio="none" height="70"><path d="M0 20V12C25 2 55 20 100 4V20Z" fill="var(--wine)"/><path d="M0 10C25 0 55 18 100 2" stroke="var(--wine-dark)" stroke-width=".5" fill="none"/></svg>
  <div class="footer-note">Pr No 7315824</div>
</section>

<span class="label" style="left:756px;top:38px">Envelope</span>
<section class="piece env-front">
  <div class="brand">
    <span class="mark"></span>
    <div>
      <div class="name">Dr Peter Vandell</div>
      <div class="quals">MB,ChB(WCU), FCS Urol.(CSU)</div>
      <div class="role">Urologist</div>
    </div>
  </div>
  <div class="contact" style="left:20px;top:52px">PO Box 58147<br>Brookvale 4105<br>Tel 033 418 6502</div>
  <svg class="wave" viewBox="0 0 100 20" preserveAspectRatio="none" height="60"><path d="M0 20V12C30 2 60 20 100 5V20Z" fill="var(--wine)"/><path d="M0 10C30 0 60 18 100 3" stroke="var(--wine-dark)" stroke-width=".5" fill="none"/></svg>
</section>

<section class="piece env-back">
  <svg viewBox="0 0 399 211">
    <rect x="0" y="0" width="399" height="211" fill="var(--paper)"/>
    <path d="M0 211L170 110Q199 95 228 110L399 211" fill="none" stroke="var(--fold)" stroke-width="1"/>
    <path d="M0 0H399V58Q200 100 0 80Z" fill="var(--wine)"/>
    <path d="M0 80Q200 100 399 58" fill="none" stroke="var(--wine-dark)" stroke-width="2"/>
    <text class="flap-name" x="200" y="44" text-anchor="middle" font-size="10">Dr Peter Vandell</text>
    <path d="M0 110Q110 150 200 130T399 112V160Q200 180 0 150Z" fill="var(--wine)"/>
    <text class="flap-name" x="200" y="146" text-anchor="middle" font-size="10">Dr Peter Vandell</text>
  </svg>
</section>

</body>
</html>
```